Plakat-Design für Tora-Unterricht einer Jüdischen Gemeinde
Zielgruppe
Wir sind die Jüdische Gemeinde.(synagogenverein Talbrück.
Wir organisieren einen Tora-Unterricht.
Zielgruppe sind Gemeindemitglieder(Männer und Frauen)die meisten aus der ehemaligen Sowjetunion, 50 Jahre aufwärts. Russischsprachig.
Die Plakate sollen in der Gemeinde hängen und so viele wie es geht ansprechen.
Aufgabenstellung
Plakat in russischer Sprache. Im folgenden steht der Text mit deutscher Übersetzung. Die Übersetzung dient nur zu Ihrer Information/Orientierung. Nur bei der Zeile mit Anführungsstrichen bleibt der deutsche Text:
Цикл лекций с раввином Элиэзер Розенфельд - Vortragsreihe von Rabbiner Elieser Rosenfeld
'Свет над морем-Licht über dem Meer'
По четвергам в 13.00 - donnerstags um 13:00 Uhr
С переводом на русский язык Светланы Мирошник - mit Übersetzung ins russische von Frau Swetlana Miroschnik
Приходите все! - Alle sind herzlich willkommen!
Вас ожидают увлека тельные уроки Торы а также интересные путешествия и экскурсии.- Euch erwarten spannende Tora Unterrichte und auch interessante Ausflüge und Besichtigung

```html
<!DOCTYPE html>
<html lang="ru">
<head>
<meta charset="utf-8">
<title>Свет над морем — плакаты</title>
<link rel="stylesheet" href="https://fonts.googleapis.com/css2?family=Open+Sans:wght@300;600;700;800&display=swap">
<style>
  :root {
    --backdrop-top: #ffffff;
    --backdrop-bottom: #b5b5b5;
    --band: #000000;
    --ink: #161616;
    --ink-soft: #5a5650;
    --accent: #5e7c96;
    --paper-white: #ffffff;
    --sea-deep: #5f7688;
    --sea-light: #a9b8bf;
    --sand: #d9c8a6;
    --parchment: #eadcbc;
  }
  * { margin: 0; padding: 0; box-sizing: border-box; }
  html, body { width: 1200px; height: 1189px; overflow: hidden; }
  body {
    position: relative;
    font-family: "Open Sans", Arial, sans-serif;
    background: linear-gradient(to bottom, var(--backdrop-top) 0 669px, var(--backdrop-bottom) 669px 100%);
  }
  .poster {
    position: absolute;
    width: 461px;
    height: 647px;
    overflow: hidden;
  }
  .poster--left { left: 107px; top: 372px; }
  .poster--right { left: 633px; top: 139px; }

  .poster__photo {
    position: absolute; left: 0; top: 0;
    width: 100%; height: 481px;
    background:
      radial-gradient(ellipse 60% 30% at 70% 42%, rgba(240,225,200,.55), transparent 70%),
      linear-gradient(to bottom, var(--sea-light) 0%, var(--sea-deep) 18%, var(--sea-light) 34%, var(--sea-deep) 42%, var(--sand) 55%, var(--parchment) 72%, var(--sand) 100%);
  }
  .poster__text { position: absolute; left: 0; width: 100%; text-align: center; }

  .poster__series {
    top: 46px;
    font-size: 15.5px; font-weight: 700; line-height: 19px;
    color: var(--ink); text-transform: uppercase; letter-spacing: .2px;
  }
  .poster__title {
    top: 87px;
    font-size: 35px; font-weight: 800; line-height: 48px;
    color: var(--ink); text-transform: uppercase;
  }
  .poster__subtitle {
    top: 131px;
    font-size: 27px; font-weight: 300; line-height: 38px;
    color: var(--paper-white);
  }
  .poster__schedule {
    position: absolute; left: 40px; top: 242px;
  }
  .poster__day {
    font-size: 24px; font-weight: 800; line-height: 34px; color: var(--ink);
  }
  .poster__translation {
    font-size: 14.5px; font-weight: 700; line-height: 21px; color: var(--ink-soft);
  }

  .poster__band {
    position: absolute; left: 0; top: 481px;
    width: 100%; height: 166px;
    background: var(--band);
    text-align: center;
  }
  .poster__call {
    margin-top: 20px;
    font-size: 24px; font-weight: 700; letter-spacing: 3px; line-height: 34px;
  }
  .poster__invite {
    margin-top: 2px;
    font-size: 17.5px; font-weight: 700; line-height: 24px;
  }
  .poster--left .poster__call { color: var(--paper-white); }
  .poster--left .poster__invite { color: var(--accent); }
  .poster--right .poster__call { color: var(--accent); }
  .poster--right .poster__invite { color: var(--paper-white); }
</style>
</head>
<body>

  <article class="poster poster--left">
    <div class="poster__photo" role="img" aria-label="Фото: морская гладь, переходящая в свиток Торы с золотым пером"></div>
    <p class="poster__text poster__series">Цикл лекций с раввином<br>Элиэзером Розенфельдом</p>
    <h1 class="poster__text poster__title">„Свет над морем“</h1>
    <p class="poster__text poster__subtitle">- Licht über dem Meer -</p>
    <div class="poster__schedule">
      <p class="poster__day">По четвергам в 13.00</p>
      <p class="poster__translation">С переводом на русский язык<br>Светланы Мирошник</p>
    </div>
    <div class="poster__band">
      <p class="poster__call">ПРИХОДИТЕ ВСЕ!</p>
      <p class="poster__invite">Вас ожидают увлекательные<br>уроки Торы а также интересные<br>путешествия и экскурсии.</p>
    </div>
  </article>

  <article class="poster poster--right">
    <div class="poster__photo" role="img" aria-label="Фото: морская гладь, переходящая в свиток Торы с золотым пером"></div>
    <p class="poster__text poster__series">Цикл лекций с раввином<br>Элиэзером Розенфельдом</p>
    <h1 class="poster__text poster__title">„Свет над морем“</h1>
    <p class="poster__text poster__subtitle">- Licht über dem Meer -</p>
    <div class="poster__schedule">
      <p class="poster__day">По четвергам в 13.00</p>
      <p class="poster__translation">С переводом на русский язык<br>Светланы Мирошник</p>
    </div>
    <div class="poster__band">
      <p class="poster__call">ПРИХОДИТЕ ВСЕ!</p>
      <p class="poster__invite">Вас ожидают увлекательные<br>уроки Торы а также интересные<br>путешествия и экскурсии.</p>
    </div>
  </article>

</body>
</html>
```